Nana Bo's needs your help creating a clean, simple, possibly vintage style label for a natural rem...

We need a label for a new product to be sold in local stores. It will be a bottle of fresh Elderberry Syrup which is a natural remedy for the flu, colds, and allergies. Our syrup is different from others in the market as it is fresh, needs to be refrigerated, and does not include preservatives, added sugar, alcohol, or anything artificial. We would like a label with easy to read text, with a clean or vintage look. We would like a 3 inch by 3 inch circle front label with mostly text, not too busy, and possibly a branch of elderberries may be included. We also need a 3 inch by 3 inch circle label for the back of the bottle with the nutrition facts, ingredients, dosage, and specific text. Both labels should be lighter in (background) color to stand out from the dark purple liquid inside. We're leaning towards black for the main text, but open to other ideas that are neutral and not too flashy.The final design should be clear, clean, making the main text visible if in a grocery store refrigerator. It should appeal to all, but mostly to natural minded mothers.
Natural minded mothers

```html
<!DOCTYPE html>
<html lang="en">
<head>
<meta charset="utf-8">
<title>Nana Bo's Elderberry Syrup – Front Label</title>
<link href="https://fonts.googleapis.com/css2?family=Kaushan+Script&family=EB+Garamond:wght@400;500&display=swap" rel="stylesheet">
<style>
  :root {
    --page-bg: #eceeef;
    --label-light: #f2a23c;
    --label-mid: #e38a24;
    --label-deep: #c8701c;
    --ink: #141210;
    --ring: #2a1e12;
    --berry-dark: #3b2a22;
    --berry-mid: #7a5533;
  }
  * { margin: 0; padding: 0; box-sizing: border-box; }
  html, body {
    width: 1200px;
    height: 1200px;
    overflow: hidden;
    background: var(--page-bg);
  }
  .canvas {
    position: relative;
    width: 1200px;
    height: 1200px;
  }
  .front-label {
    position: absolute;
    left: 100px;
    top: 100px;
    width: 1000px;
    height: 1000px;
    border-radius: 50%;
    background:
      radial-gradient(circle at 35% 30%, var(--label-light) 0%, transparent 55%),
      radial-gradient(circle at 70% 75%, var(--label-deep) 0%, transparent 60%),
      var(--label-mid);
    color: var(--ink);
    text-align: center;
  }
  .label-ring {
    position: absolute;
    left: 20px;
    top: 20px;
    width: 960px;
    height: 960px;
    border-radius: 50%;
    border: 3px solid var(--ring);
  }
  .line {
    position: absolute;
    left: 0;
    width: 100%;
    transform: translateY(-50%);
  }
  .brand-name {
    top: 210px;
    font-family: "Kaushan Script", cursive;
    font-size: 84px;
  }
  .product-name {
    top: 394px;
    font-family: "Kaushan Script", cursive;
    font-size: 112px;
    letter-spacing: -1px;
  }
  .berry-art {
    position: absolute;
    left: 342px;
    top: 470px;
    width: 316px;
    height: 186px;
  }
  .description {
    font-family: "EB Garamond", serif;
    font-size: 34px;
    line-height: 1;
  }
  .ingredients-1 { top: 717px; }
  .ingredients-2 { top: 763px; }
  .claims {
    font-family: "EB Garamond", serif;
    font-size: 29px;
  }
  .claims-1 { top: 826px; }
  .claims-2 { top: 864px; }
  .net-weight {
    top: 926px;
    font-family: "EB Garamond", serif;
    font-size: 30px;
  }
</style>
</head>
<body>
<main class="canvas">
  <section class="front-label">
    <div class="label-ring"></div>
    <p class="line brand-name">Nana Bo's</p>
    <h1 class="line product-name">Elderberry Syrup</h1>
    <svg class="berry-art" viewBox="0 0 316 186" role="img" aria-label="Illustration of an elderberry cluster with leaves">
      <defs>
        <radialGradient id="berryTone" cx="50%" cy="50%" r="50%">
          <stop offset="0%" stop-color="var(--berry-mid)"/>
          <stop offset="100%" stop-color="var(--berry-dark)" stop-opacity="0.85"/>
        </radialGradient>
      </defs>
      <ellipse cx="158" cy="100" rx="140" ry="78" fill="url(#berryTone)" opacity="0.55"/>
    </svg>
    <p class="line description ingredients-1">made with organic elderberries and spices</p>
    <p class="line description ingredients-2">and local Texas raw honey</p>
    <p class="line claims claims-1">immune boosting*, natural remedy for the</p>
    <p class="line claims claims-2">flu, colds, and allergies*</p>
    <p class="line net-weight">NET WT 8 FL OZ</p>
  </section>
</main>
</body>
</html>
```